Mortgage Broking boutique Business

I’m wanting a revamped look to my existing business card design. I do like the black and silver but happy to have other colours introduced based on your creation. I’ve attached a copy of my current card so you can have a starting point updated details noted brloe. I deal with high net worth individuals so need my card to be sophisticated, classy that gives off a classy vibe

Target Market(s)

High net worth, wealthy

Industry/Entity Type

Mortgage Brokerage

Contact Information for Business Card

Job title: Finance Executive
Phone: +61 7 3287 4419
Mobile: 0471 352 608
Email: marcus@quillbrookcapital.com.au
Web: www.quillbrookcapital.com.au
Address: level 36 Tindale Court, 58 Harwick St Brisbane QLD 4000

Font styles to use
Other font styles liked:
• Helvetica

Colors

Designer to choose colors to be used in the design.

Requirements
Must have
• Use my existing card design as a starting point

```html
<!DOCTYPE html>
<html lang="en">
<head>
<meta charset="utf-8">
<title>Quillbrook Capital – Business Card</title>
<link rel="stylesheet" href="https://fonts.googleapis.com/css2?family=Montserrat:wght@300;500;600&family=Open+Sans:wght@400&display=swap">
<style>
  :root {
    --backdrop: #cfcac3;
    --card-black: #000000;
    --ink-white: #ffffff;
    --silver: #b9b6b6;
    --silver-dark: #5a5757;
    --silver-light: #e9e6ee;
    --url-grey: #a9a6a6;
  }
  html, body {
    margin: 0;
    padding: 0;
    width: 1200px;
    height: 1200px;
    overflow: hidden;
    background: var(--backdrop);
  }
  .canvas {
    position: relative;
    width: 1200px;
    height: 1200px;
  }
  .card {
    position: absolute;
    left: 300px;
    width: 600px;
    height: 342px;
    display: block;
  }
  .card--front { top: 206px; }
  .card--back { top: 651px; }
  .card-bg { fill: var(--card-black); }
  .frame { fill: none; stroke: var(--ink-white); stroke-width: 1.4; }
  .brand { font-family: "Montserrat", sans-serif; font-weight: 500; fill: var(--ink-white); }
  .brand--back { fill: var(--silver); }
  .holder-name { font-family: "Montserrat", sans-serif; font-weight: 600; font-size: 30px; fill: var(--ink-white); }
  .holder-title { font-family: "Montserrat", sans-serif; font-weight: 300; font-size: 17px; fill: var(--ink-white); }
  .contact { font-family: "Open Sans", sans-serif; font-size: 19px; fill: var(--ink-white); }
  .web { font-family: "Montserrat", sans-serif; font-weight: 600; font-size: 23px; fill: var(--url-grey); }
  .icon-disc { fill: var(--ink-white); }
  .icon-glyph { fill: var(--card-black); }
  .stripe-white { fill: var(--ink-white); }
</style>
</head>
<body>
<div class="canvas">

  <svg class="card card--front" viewBox="0 0 600 342" xmlns="http://www.w3.org/2000/svg">
    <defs>
      <linearGradient id="silverBand" x1="0" y1="0" x2="1" y2="0">
        <stop offset="0" stop-color="#4d4a4a"/>
        <stop offset="0.3" stop-color="#d8d6de"/>
        <stop offset="0.55" stop-color="#8f8c8c"/>
        <stop offset="0.8" stop-color="#efe9ec"/>
        <stop offset="1" stop-color="#5e5a5a"/>
      </linearGradient>
    </defs>
    <rect class="card-bg" width="600" height="342"/>
    <path class="frame" d="M21 310 V34 Q21 22 33 22 H566 Q578 22 578 34 V310"/>
    <line class="frame" x1="21" y1="177" x2="404" y2="177"/>

    <text class="brand" x="30" y="64" font-size="37">QUILLBROOK</text>
    <text class="brand" x="75" y="89" font-size="37" textLength="0" style="font-size:22px">CAPITAL</text>

    <text class="holder-name" x="568" y="161" text-anchor="end">MARCUS VELL</text>
    <text class="holder-title" x="568" y="184" text-anchor="end">Finance Executive</text>

    <g transform="translate(40 198)">
      <circle class="icon-disc" r="10"/>
      <path class="icon-glyph" d="M-5 -5 l3 -1 l2 4 l-2 2 q1 3 4 4 l2 -2 l4 2 l-1 3 q-9 0 -12 -12z"/>
    </g>
    <text class="contact" x="60" y="204">+61 7 3287 4419</text>

    <g transform="translate(40 224)">
      <rect class="icon-disc" x="-8" y="-11" width="16" height="22" rx="4"/>
      <rect class="icon-glyph" x="-4.5" y="-7" width="9" height="12" rx="1"/>
    </g>
    <text class="contact" x="60" y="230">0471 352 608</text>

    <g transform="translate(40 251)">
      <circle class="icon-disc" r="10"/>
      <rect class="icon-glyph" x="-6" y="-4" width="12" height="8"/>
      <path d="M-6 -4 L0 1 L6 -4" fill="none" stroke="#fff" stroke-width="1.2"/>
    </g>
    <text class="contact" x="58" y="257">marcus@quillbrookcapital.com.au</text>

    <g transform="translate(40 278)">
      <circle class="icon-disc" r="10"/>
      <path class="icon-glyph" d="M0 7 C-4 2 -5 0 -5 -2 A5 5 0 0 1 5 -2 C5 0 4 2 0 7z"/>
      <circle class="icon-disc" cy="-2" r="1.8"/>
    </g>
    <text class="contact" x="58" y="284">level 36 Tindale Court,</text>
    <text class="contact" x="58" y="306">58 Harwick St Brisbane QLD 4000</text>

    <polygon fill="url(#silverBand)" points="0,310 160,310 178,326 600,326 600,342 0,342"/>
    <polygon class="stripe-white" points="170,311 600,311 600,320 180,320"/>
  </svg>

  <svg class="card card--back" viewBox="0 0 600 342" xmlns="http://www.w3.org/2000/svg">
    <defs>
      <linearGradient id="silverBandBack" x1="0" y1="0" x2="1" y2="0">
        <stop offset="0" stop-color="#4d4a4a"/>
        <stop offset="0.3" stop-color="#d8d6de"/>
        <stop offset="0.55" stop-color="#8f8c8c"/>
        <stop offset="0.8" stop-color="#efe9ec"/>
        <stop offset="1" stop-color="#5e5a5a"/>
      </linearGradient>
    </defs>
    <rect class="card-bg" width="600" height="342"/>
    <text class="brand brand--back" x="300" y="171" font-size="56" text-anchor="middle">QUILLBROOK</text>
    <text class="brand brand--back" x="300" y="213" font-size="38" text-anchor="middle">CAPITAL</text>
    <text class="web" x="300" y="293" text-anchor="middle">www.quillbrookcapital.com.au</text>
    <polygon fill="url(#silverBandBack)" points="0,310 160,310 178,326 600,326 600,342 0,342"/>
    <polygon class="stripe-white" points="170,311 600,311 600,320 180,320"/>
  </svg>

</div>
</body>
</html>
```